MARVELTRUST web-presence redisign

We would like to have our existing web-presence redesigned. Have a look at www.pelbrika-example.ch (please use explorer). To the existing 11 pages we would add one more.

```html
<!DOCTYPE html>
<html lang="de">
<head>
<meta charset="utf-8">
<title>CLARDENT Zahnarztpraxis</title>
<link rel="stylesheet" href="https://fonts.googleapis.com/css2?family=Libre+Baskerville:wght@400;700&family=Open+Sans:ital,wght@0,300;0,400;1,300;1,400&display=swap">
<style>
  :root {
    --night-dark: #2e1c11;
    --night-mid: #5a3a22;
    --night-warm: #8a5a30;
    --ribbon: #e3a64b;
    --ribbon-tail: #b8722c;
    --ribbon-edge: #c98a38;
    --nav-text: #6a3817;
    --phone-box: #4a2f1e;
    --white: #ffffff;
    --footer-bg: #cfcfcf;
    --footer-text: #222222;
  }
  * { margin: 0; padding: 0; box-sizing: border-box; }
  html, body { width: 1200px; height: 715px; overflow: hidden; }
  body { font-family: "Open Sans", Arial, sans-serif; background: var(--footer-bg); }

  .hero {
    position: relative;
    width: 1200px;
    height: 625px;
    overflow: hidden;
    background:
      radial-gradient(ellipse 260px 160px at 330px 300px, rgba(190,130,60,.55), transparent 70%),
      radial-gradient(ellipse 300px 120px at 150px 260px, rgba(160,100,45,.45), transparent 70%),
      radial-gradient(ellipse 220px 140px at 500px 470px, rgba(170,110,55,.4), transparent 70%),
      radial-gradient(ellipse 400px 200px at 900px 120px, rgba(120,80,45,.45), transparent 70%),
      linear-gradient(180deg, var(--night-dark) 0%, var(--night-mid) 45%, var(--night-warm) 62%, var(--night-dark) 100%);
  }

  .phone {
    position: absolute; left: 849px; top: 0; width: 192px; height: 34px;
    background: var(--phone-box);
    display: flex; align-items: center; gap: 8px; padding-left: 17px;
    color: var(--white); font-style: italic; font-weight: 300; font-size: 16px;
  }
  .phone svg { width: 14px; height: 16px; }

  .brand {
    position: absolute; left: 450px; top: 40px; width: 310px;
    display: flex; align-items: center; gap: 14px;
    color: var(--white); font-family: "Libre Baskerville", Georgia, serif; font-weight: 400;
  }
  .brand-mark { width: 40px; height: 40px; border-radius: 50%; background: var(--ribbon); flex: none; }
  .brand-name { font-size: 34px; letter-spacing: 3px; line-height: 1; }
  .brand-sub { font-size: 24px; line-height: 1.3; }

  .nav-ribbon { position: absolute; left: 160px; top: 136px; width: 880px; height: 60px; }
  .nav-list {
    position: absolute; left: 193px; top: 145px; width: 813px; height: 50px;
    display: flex; justify-content: center; list-style: none;
  }
  .nav-list li {
    display: flex; align-items: center; padding: 0 23px;
    font-family: "Libre Baskerville", Georgia, serif; font-weight: 700; font-size: 14.5px;
    color: var(--nav-text); border-left: 1px solid var(--ribbon-edge);
  }
  .nav-list li:first-child { border-left: none; }
  .nav-list .has-sub::after {
    content: ""; width: 7px; height: 7px; border-radius: 50%;
    background: var(--nav-text); margin-left: 3px; margin-top: 5px;
  }

  .photo {
    position: absolute; left: 595px; top: 205px; width: 605px; height: 420px;
    background: radial-gradient(ellipse 300px 260px at 50% 55%, #c9a58a 0%, #a98a78 40%, rgba(120,100,100,.6) 70%, transparent 90%);
  }

  .intro { position: absolute; left: 157px; top: 343px; width: 440px; text-align: center; color: var(--white); }
  .doctor {
    display: flex; align-items: center; justify-content: center; gap: 10px;
    font-style: italic; font-weight: 300; font-size: 16px;
  }
  .doctor::before, .doctor::after {
    content: ""; width: 100px; border-top: 1px dashed var(--white);
  }
  .mission { margin-top: 14px; font-weight: 300; font-size: 25px; line-height: 29px; }
  .cta {
    display: inline-block; margin-top: 18px; width: 224px; height: 41px; line-height: 38px;
    border: 1px solid var(--white); color: var(--white); text-decoration: none;
    font-family: "Libre Baskerville", Georgia, serif; font-weight: 700; font-size: 22px;
  }

  .site-footer {
    height: 90px; display: flex; flex-direction: column; justify-content: center; align-items: center;
    gap: 4px; color: var(--footer-text); font-size: 13px; line-height: 16px;
  }
</style>
</head>
<body>
  <header class="hero">
    <div class="phone">
      <svg viewBox="0 0 14 16" aria-hidden="true"><path d="M3 1 L5.5 1 L6.5 5 L4.8 6.2 Q6 9.8 8.8 11.3 L10 9.6 L13 10.8 L13 13.5 Q11 15.5 7.5 13.5 Q2 10 1.2 4 Q1 2 3 1 Z" fill="#fff"/></svg>
      +41 (0)44 555 01 23
    </div>

    <div class="brand">
      <span class="brand-mark"></span>
      <div>
        <div class="brand-name">CLARDENT</div>
        <div class="brand-sub">Zahnarztpraxis</div>
      </div>
    </div>

    <svg class="nav-ribbon" viewBox="0 0 880 60" aria-hidden="true">
      <polygon points="2,1 64,1 64,51 12,51 20,26" fill="var(--ribbon-tail)"/>
      <polygon points="878,1 816,1 816,51 868,51 860,26" fill="var(--ribbon-tail)"/>
      <rect x="33" y="9" width="814" height="50" fill="var(--ribbon)"/>
      <line x1="40" y1="15" x2="840" y2="15" stroke="#9c6228" stroke-dasharray="3 2" stroke-width="1"/>
      <line x1="40" y1="53" x2="840" y2="53" stroke="#9c6228" stroke-dasharray="3 2" stroke-width="1"/>
    </svg>
    <nav>
      <ul class="nav-list">
        <li>HOME</li>
        <li>ZAHNMEDIZIN</li>
        <li class="has-sub">DENTALHYGIENE</li>
        <li>TEAM</li>
        <li>KONTAKT</li>
      </ul>
    </nav>

    <div class="photo" role="img" aria-label="Photo of a smiling couple leaning their heads together"></div>

    <section class="intro">
      <p class="doctor">Dr. med. Laura Meier-Keller</p>
      <p class="mission">It is our goal to improve your wellbeing. You will enjoy the beauty of everyday life with healthy teeth and laugh heartily in every situation.</p>
      <a class="cta" href="#">Call to Action</a>
    </section>
  </header>

  <footer class="site-footer">
    <p>Add: Lindenweg 12 CH-8000 Musterstadt &nbsp;-&nbsp; Email : info@clardent-example.ch</p>
    <p>All rights reserved © 2014 - Privacy Policy</p>
  </footer>
</body>
</html>
```